Luxury skin care/beauty salon needs a fresh wordpress website makeover

Today we have a wordpress site that has served us well, and we want to stay with wordpress, but we need a new up to date fresh look, with an inviting and enticing front, and look that just draws people in to book an appoint for luxury beauty treatment.

The salon consists of beautisian/skin specialint, a cosmetical nurse, and a doctor, - so top notch expertice within skin care and beauty treatment.

- The site should be integrated with Postwren (which we currently do not use.

- The site should further be able to "show prices for treatments" in a manner that matches the new website in style and layout, - we do show prices today via ex. the booking module from a vendor, but its done via iFrame

- booking needs to be very easy and intuitive, and the site needs to be response, since 75% of our customers use Ipad or mobile phone while booking

- the colours of the logo and style for the company today is primarily gold and black, and the shop is kept in a minimalistic style

- we have fresh newly made professional pictures made, and we can also later supply a video for ex. a landing page

- we have a license for Framewick if that can be utilized

- we need to be able to translate all elements into minimum Norwegian

- we use QL and Snapvale today to promote our services, if that can be incorporated, that would be a promotion plus

today we have the following pages
- main page
- a treatment page, where treatments are in more detail explained, this also doubles as pricelist ... we might look to discard this, since its manually updated and is not the master ... the master is the booking system, which also contains princes
- a portfolio page, seperated into types of treatments, this page also has one element of Snapvale which is one of the prime social media channals.
- a team member page, that presents the staff
- a contact us page
- a booking page ( that uses the national available booking system that we want to keep, but present in a different manner if possible) .. including gift card

we are not nessesarily looking to keep all pages, if the new design comes up with a more proffesional and smoother look, so this is debatable, so i have left the "How many web pages do you need designed?" to 4 pages .. again debatable

The final design should communicate luxury and professional skincare and beauty treatments, and easy booking.

Target Market(s)

Women or men that want to book a beauty or skin care treatment

Industry/Entity Type

Beauty and skin care salon

Coding

Coded - Design and coding required

Number of Pages Required

4 page

Colors

Designer to choose colors to be used in the design.

Requirements
Must have
• booking system, a connection to postwren, ability to change wording/language (Norwegian)
Nice to have
• video background, if it compliments the design
Should not have
• a new booking platform, we want to stick with the one we have

```html
<!DOCTYPE html>
<html lang="en">
<head>
<meta charset="utf-8">
<title>Velor – Luxury Skin Care Website</title>
<link href="https://fonts.googleapis.com/css2?family=Montserrat:wght@400;600;700&family=Lato:wght@400;700&display=swap" rel="stylesheet">
<style>
  :root{
    --gold:#c9a24a;
    --gold-dark:#a9832f;
    --black:#0c0c0c;
    --ink:#1b1b1b;
    --white:#ffffff;
    --stage:#f1f1f1;
    --hero-a:#2b2520;
    --hero-b:#6b5a4a;
    --photo-a:#3a3029;
    --photo-b:#a88e72;
    --skin-a:#c8a58e;
    --skin-b:#8e6f5e;
  }
  *{box-sizing:border-box;margin:0;padding:0}
  html,body{width:807px;height:1200px;overflow:hidden;background:var(--stage)}
  body{font-family:'Lato',sans-serif;position:relative}

  .page{
    --bg:var(--white);--text:var(--ink);--muted:#6d6d6d;--line:#dcdcdc;--soft:#f6f6f6;
    position:absolute;top:21px;width:371px;height:1158px;background:var(--bg);color:var(--text);
    overflow:hidden;box-shadow:0 1px 4px rgba(0,0,0,.12);display:flex;flex-direction:column
  }
  .page--light{left:27px}
  .page--dark{left:409px;--bg:var(--black);--text:var(--white);--muted:#a9a9a9;--line:#333;--soft:#161616}

  .heading{font-family:'Montserrat',sans-serif;font-weight:700;letter-spacing:.06em;text-transform:uppercase}
  .btn{display:inline-block;font-family:'Montserrat',sans-serif;font-size:5px;font-weight:600;letter-spacing:.08em;
       text-transform:uppercase;padding:4px 9px;border:1px solid var(--text);color:var(--text)}
  .btn--gold{background:var(--gold);border-color:var(--gold);color:var(--black)}
  .photo{display:block}
  .lines span{display:block;font-size:5px;line-height:7.5px;color:var(--muted)}

  /* hero */
  .hero{position:relative;height:180px;background:linear-gradient(120deg,var(--hero-a) 0%,var(--hero-b) 55%,var(--hero-a) 100%)}
  .topbar{position:absolute;top:0;left:0;right:0;height:26px;background:rgba(0,0,0,.85);display:flex;align-items:center;padding:0 12px}
  .brand{font-family:'Montserrat',sans-serif;font-weight:700;font-size:11px;letter-spacing:.12em;color:var(--gold)}
  .topbar__nav{margin-left:auto;display:flex;gap:9px;align-items:center}
  .topbar__nav a{font-size:5px;color:#fff;text-decoration:none;font-family:'Montserrat',sans-serif;letter-spacing:.05em}
  .topbar__contact{position:absolute;top:3px;right:12px;font-size:4px;color:#bbb}
  .hero__copy{position:absolute;left:0;right:0;top:74px;text-align:center;color:#fff}
  .hero__title{font-size:15px;color:#fff}
  .hero__sub{font-size:5.5px;margin:5px 0 8px;color:#ddd}

  /* welcome */
  .welcome{height:140px;display:flex;gap:16px;padding:18px 26px 0}
  .welcome__photo{width:82px;height:106px;background:linear-gradient(160deg,var(--photo-a),var(--photo-b))}
  .welcome__text{flex:1;padding-top:6px}
  .section-title{font-size:9px;color:var(--text)}
  .welcome__text .lines{margin:7px 0 9px}

  /* treatments */
  .treatments{height:236px;padding-top:10px;text-align:center}
  .rule{width:24px;height:1px;background:var(--gold);margin:4px auto 0}
  .treat-row{display:flex;justify-content:center;align-items:flex-start;gap:18px;margin-top:14px;position:relative}
  .treat-row::before{content:"";position:absolute;left:30px;right:30px;top:15px;height:1px;background:var(--line)}
  .treat{display:flex;flex-direction:column;align-items:center;gap:5px;position:relative}
  .treat__icon{width:30px;height:30px;border-radius:50%;border:1px solid var(--gold);background:var(--bg);display:flex;align-items:center;justify-content:center}
  .treat--active .treat__icon{width:40px;height:40px;margin-top:-5px;background:var(--black);border:2px solid var(--gold)}
  .page--dark .treat--active .treat__icon{background:var(--white)}
  .treat__label{font-size:4.5px;font-family:'Montserrat',sans-serif;letter-spacing:.05em;text-transform:uppercase;color:var(--text)}
  .treat-detail{display:flex;gap:14px;padding:16px 26px 0;text-align:left}
  .treat-detail__list{flex:1}
  .treat-detail__name{font-size:6.5px;font-weight:700;margin-bottom:6px}
  .price-grid{display:grid;grid-template-columns:1fr 1fr 1fr;gap:3px 8px;margin-bottom:10px}
  .price-grid span{font-size:4.5px;color:var(--muted)}
  .treat-detail__photo{width:132px;height:92px;background:linear-gradient(140deg,#e9e6e2,#b8aba0)}
  .page--dark .treat-detail__photo{background:linear-gradient(140deg,#3a3532,#8d8078)}

  /* portfolio */
  .portfolio{height:256px;background:var(--soft);padding-top:14px;text-align:center}
  .tabs{display:flex;justify-content:center;gap:11px;margin:9px 0 10px}
  .tabs span{font-size:4.5px;font-family:'Montserrat',sans-serif;text-transform:uppercase;color:var(--muted)}
  .tabs .is-active{color:var(--text);border-bottom:1px solid var(--gold)}
  .gallery{display:grid;grid-template-columns:repeat(4,72px);grid-auto-rows:70px;gap:6px;justify-content:center;margin-bottom:12px}
  .gallery .photo:nth-child(odd){background:linear-gradient(150deg,var(--skin-a),var(--skin-b))}
  .gallery .photo:nth-child(even){background:linear-gradient(150deg,#b7a496,#6f5b50)}

  /* testimonials */
  .testimonials{height:130px;background:var(--gold);text-align:center;padding-top:22px;color:var(--black)}
  .testimonials .section-title{color:var(--black)}
  .testimonials .lines{margin-top:12px}
  .testimonials .lines span{color:#3a2d10;font-size:5.5px;line-height:8px}
  .dots{display:flex;gap:4px;justify-content:center;margin-top:12px}
  .dots i{width:4px;height:4px;border-radius:50%;background:rgba(0,0,0,.3)}
  .dots i:first-child{background:var(--black)}

  /* signup */
  .signup{height:100px;display:flex;align-items:center;gap:16px;padding:0 26px}
  .signup__partner{display:flex;align-items:center;gap:5px;font-family:'Lato',sans-serif;font-weight:700;font-size:8px;color:var(--text)}
  .signup__partner i{width:30px;height:30px;border-radius:50%;background:var(--text)}
  .signup__form{flex:1}
  .signup__row{display:flex;margin-top:8px}
  .signup__input{flex:1;height:14px;border:1px solid var(--line);font-size:4.5px;color:var(--muted);padding:4px 5px;background:var(--bg)}
  .signup__row .btn{border-radius:0;padding:4px 8px}

  /* footer */
  .footer{height:116px;background:var(--black);color:#fff;padding:16px 26px 0;display:flex;gap:16px;position:relative}
  .page--dark .footer{border-top:1px solid #222}
  .footer__brands{width:72px;display:flex;flex-direction:column;gap:10px}
  .footer__brands span{font-family:'Montserrat',sans-serif;font-weight:700;font-size:8px;color:#fff;letter-spacing:.04em}
  .footer__col{flex:1}
  .footer__col h4{font-family:'Montserrat',sans-serif;font-size:5px;letter-spacing:.08em;text-transform:uppercase;color:var(--gold);margin-bottom:5px}
  .footer__col span{display:flex;align-items:center;gap:3px;font-size:4.5px;line-height:7.5px;color:#bbb}
  .footer__copy{position:absolute;left:26px;right:26px;bottom:7px;border-top:1px solid #2a2a2a;padding-top:4px;font-size:4px;color:#888}
</style>
</head>
<body>

<!-- light theme page -->
<main class="page page--light">
  <header class="hero photo" role="img" aria-label="Photo of a client receiving a facial treatment in the salon">
    <div class="topbar">
      <span class="brand">VELOR</span>
      <span class="topbar__contact">+47 000 00 000 · hello@velor.no</span>
      <nav class="topbar__nav">
        <a>Home</a><a>Treatments</a><a>Portfolio</a><a>Team</a><a>Contact</a>
        <span class="btn btn--gold">Book Now</span>
      </nav>
    </div>
    <div class="hero__copy">
      <h1 class="heading hero__title">Luxury Skin Care</h1>
      <p class="hero__sub">Expert treatments by skin therapists, nurses and doctors</p>
      <span class="btn btn--gold">Book Treatment</span>
    </div>
  </header>

  <section class="welcome">
    <div class="welcome__photo photo" role="img" aria-label="Photo of the salon team standing by the front desk"></div>
    <div class="welcome__text">
      <h2 class="heading section-title">Welcome to Velor</h2>
      <div class="lines">
        <span>Our salon brings together a skin specialist, a cosmetic</span>
        <span>nurse and a doctor, offering top expertise in skin care</span>
        <span>and beauty treatments in a calm, refined setting.</span>
        <span>Every visit is tailored to your skin and your goals.</span>
      </div>
      <span class="btn">Read More</span>
    </div>
  </section>

  <section class="treatments">
    <h2 class="heading section-title">Our Treatment</h2>
    <div class="rule"></div>
    <div class="treat-row">
      <div class="treat"><span class="treat__icon"></span><span class="treat__label">Facial</span></div>
      <div class="treat"><span class="treat__icon"></span><span class="treat__label">Peeling</span></div>
      <div class="treat treat--active"><span class="treat__icon"></span><span class="treat__label">Skin</span></div>
      <div class="treat"><span class="treat__icon"></span><span class="treat__label">Brows</span></div>
      <div class="treat"><span class="treat__icon"></span><span class="treat__label">Lashes</span></div>
    </div>
    <div class="treat-detail">
      <div class="treat-detail__list">
        <p class="treat-detail__name">Skin Treatment</p>
        <div class="price-grid">
          <span>Deep cleanse</span><span>Hydra facial</span><span>Micro peel</span>
          <span>LED therapy</span><span>Skin booster</span><span>Acne care</span>
          <span>Anti aging</span><span>Glow facial</span><span>Consultation</span>
        </div>
        <span class="btn">See Prices</span>
      </div>
      <div class="treat-detail__photo photo" role="img" aria-label="Photo of a nurse in a white coat in the treatment room"></div>
    </div>
  </section>

  <section class="portfolio">
    <h2 class="heading section-title">Portfolio</h2>
    <div class="rule"></div>
    <div class="tabs"><span class="is-active">All</span><span>Brows</span><span>Lashes</span><span>Lips</span><span>Skin</span><span>Body</span></div>
    <div class="gallery">
      <div class="photo" role="img" aria-label="Result photo of shaped brows"></div>
      <div class="photo" role="img" aria-label="Result photo of a hand treatment"></div>
      <div class="photo" role="img" aria-label="Result photo of lash extensions"></div>
      <div class="photo" role="img" aria-label="Result photo of a skin treatment"></div>
      <div class="photo" role="img" aria-label="Result photo of tinted brows"></div>
      <div class="photo" role="img" aria-label="Result photo of lifted lashes"></div>
      <div class="photo" role="img" aria-label="Result photo of lip treatment"></div>
      <div class="photo" role="img" aria-label="Result photo of an eye area treatment"></div>
    </div>
    <span class="btn">View More</span>
  </section>

  <section class="testimonials">
    <h2 class="heading section-title">Client Testimonials</h2>
    <div class="lines">
      <span>“Wonderful care from start to finish. My skin has never looked</span>
      <span>better and booking took less than a minute.” – Ingrid H.</span>
    </div>
    <div class="dots"><i></i><i></i><i></i></div>
  </section>

  <section class="signup">
    <span class="signup__partner"><i></i>Postwren</span>
    <div class="signup__form">
      <h2 class="heading section-title">Email Sign Up</h2>
      <div class="signup__row"><span class="signup__input">Your email address</span><span class="btn btn--gold">Sign Up</span></div>
    </div>
  </section>

  <footer class="footer">
    <div class="footer__brands"><span>Skinvera</span><span>AURIEL</span></div>
    <div class="footer__col"><h4>Explore</h4><span>Home</span><span>Treatments</span><span>Portfolio</span><span>Team</span><span>Gift Card</span></div>
    <div class="footer__col"><h4>Contact</h4>
      <span><svg width="5" height="5" viewBox="0 0 10 10"><path d="M5 0C3 0 1.5 1.5 1.5 3.5 1.5 6 5 10 5 10s3.5-4 3.5-6.5C8.5 1.5 7 0 5 0z" fill="#c9a24a"/></svg>Storgata 12, Oslo</span>
      <span><svg width="5" height="5" viewBox="0 0 10 10"><path d="M2 0l2 2.5-1 1.5c.8 1.5 1.5 2.2 3 3l1.5-1L10 8 8.5 10C4 9.5.5 6 0 1.5z" fill="#c9a24a"/></svg>+47 000 00 000</span>
      <span><svg width="5" height="5" viewBox="0 0 10 10"><rect x="0" y="2" width="10" height="6" fill="none" stroke="#c9a24a"/><path d="M0 2l5 3.5L10 2" fill="none" stroke="#c9a24a"/></svg>hello@velor.no</span>
    </div>
    <div class="footer__col"><h4>Opening Hours</h4><span>Mon – Fri 09 – 18</span><span>Saturday 10 – 16</span><span>Sunday Closed</span></div>
    <p class="footer__copy">© 2024 Velor Skin Care. All rights reserved.</p>
  </footer>
</main>

<!-- dark theme page -->
<main class="page page--dark">
  <header class="hero photo" role="img" aria-label="Photo of a client receiving a facial treatment in the salon">
    <div class="topbar">
      <span class="brand">VELOR</span>
      <span class="topbar__contact">+47 000 00 000 · hello@velor.no</span>
      <nav class="topbar__nav">
        <a>Home</a><a>Treatments</a><a>Portfolio</a><a>Team</a><a>Contact</a>
        <span class="btn btn--gold">Book Now</span>
      </nav>
    </div>
    <div class="hero__copy">
      <h1 class="heading hero__title">Luxury Skin Care</h1>
      <p class="hero__sub">Expert treatments by skin therapists, nurses and doctors</p>
      <span class="btn btn--gold">Book Treatment</span>
    </div>
  </header>

  <section class="welcome">
    <div class="welcome__photo photo" role="img" aria-label="Photo of the salon team standing by the front desk"></div>
    <div class="welcome__text">
      <h2 class="heading section-title">Welcome to Velor</h2>
      <div class="lines">
        <span>Our salon brings together a skin specialist, a cosmetic</span>
        <span>nurse and a doctor, offering top expertise in skin care</span>
        <span>and beauty treatments in a calm, refined setting.</span>
        <span>Every visit is tailored to your skin and your goals.</span>
      </div>
      <span class="btn">Read More</span>
    </div>
  </section>

  <section class="treatments">
    <h2 class="heading section-title">Our Treatment</h2>
    <div class="rule"></div>
    <div class="treat-row">
      <div class="treat"><span class="treat__icon"></span><span class="treat__label">Facial</span></div>
      <div class="treat"><span class="treat__icon"></span><span class="treat__label">Peeling</span></div>
      <div class="treat treat--active"><span class="treat__icon"></span><span class="treat__label">Skin</span></div>
      <div class="treat"><span class="treat__icon"></span><span class="treat__label">Brows</span></div>
      <div class="treat"><span class="treat__icon"></span><span class="treat__label">Lashes</span></div>
    </div>
    <div class="treat-detail">
      <div class="treat-detail__list">
        <p class="treat-detail__name">Skin Treatment</p>
        <div class="price-grid">
          <span>Deep cleanse</span><span>Hydra facial</span><span>Micro peel</span>
          <span>LED therapy</span><span>Skin booster</span><span>Acne care</span>
          <span>Anti aging</span><span>Glow facial</span><span>Consultation</span>
        </div>
        <span class="btn">See Prices</span>
      </div>
      <div class="treat-detail__photo photo" role="img" aria-label="Photo of a nurse in a white coat in the treatment room"></div>
    </div>
  </section>

  <section class="portfolio">
    <h2 class="heading section-title">Portfolio</h2>
    <div class="rule"></div>
    <div class="tabs"><span class="is-active">All</span><span>Brows</span><span>Lashes</span><span>Lips</span><span>Skin</span><span>Body</span></div>
    <div class="gallery">
      <div class="photo" role="img" aria-label="Result photo of shaped brows"></div>
      <div class="photo" role="img" aria-label="Result photo of a hand treatment"></div>
      <div class="photo" role="img" aria-label="Result photo of lash extensions"></div>
      <div class="photo" role="img" aria-label="Result photo of a skin treatment"></div>
      <div class="photo" role="img" aria-label="Result photo of tinted brows"></div>
      <div class="photo" role="img" aria-label="Result photo of lifted lashes"></div>
      <div class="photo" role="img" aria-label="Result photo of lip treatment"></div>
      <div class="photo" role="img" aria-label="Result photo of an eye area treatment"></div>
    </div>
    <span class="btn">View More</span>
  </section>

  <section class="testimonials">
    <h2 class="heading section-title">Client Testimonials</h2>
    <div class="lines">
      <span>“Wonderful care from start to finish. My skin has never looked</span>
      <span>better and booking took less than a minute.” – Ingrid H.</span>
    </div>
    <div class="dots"><i></i><i></i><i></i></div>
  </section>

  <section class="signup">
    <span class="signup__partner"><i></i>Postwren</span>
    <div class="signup__form">
      <h2 class="heading section-title">Email Sign Up</h2>
      <div class="signup__row"><span class="signup__input">Your email address</span><span class="btn btn--gold">Sign Up</span></div>
    </div>
  </section>

  <footer class="footer">
    <div class="footer__brands"><span>Skinvera</span><span>AURIEL</span></div>
    <div class="footer__col"><h4>Explore</h4><span>Home</span><span>Treatments</span><span>Portfolio</span><span>Team</span><span>Gift Card</span></div>
    <div class="footer__col"><h4>Contact</h4>
      <span><svg width="5" height="5" viewBox="0 0 10 10"><path d="M5 0C3 0 1.5 1.5 1.5 3.5 1.5 6 5 10 5 10s3.5-4 3.5-6.5C8.5 1.5 7 0 5 0z" fill="#c9a24a"/></svg>Storgata 12, Oslo</span>
      <span><svg width="5" height="5" viewBox="0 0 10 10"><path d="M2 0l2 2.5-1 1.5c.8 1.5 1.5 2.2 3 3l1.5-1L10 8 8.5 10C4 9.5.5 6 0 1.5z" fill="#c9a24a"/></svg>+47 000 00 000</span>
      <span><svg width="5" height="5" viewBox="0 0 10 10"><rect x="0" y="2" width="10" height="6" fill="none" stroke="#c9a24a"/><path d="M0 2l5 3.5L10 2" fill="none" stroke="#c9a24a"/></svg>hello@velor.no</span>
    </div>
    <div class="footer__col"><h4>Opening Hours</h4><span>Mon – Fri 09 – 18</span><span>Saturday 10 – 16</span><span>Sunday Closed</span></div>
    <p class="footer__copy">© 2024 Velor Skin Care. All rights reserved.</p>
  </footer>
</main>

</body>
</html>
```